Pixvane Set Up Ads for KELBY Property Management Company

We need a set of 6 ads of the following sizes created for Pixvane:

Medium rectangle: 300×250
Leaderboard: 728×90
Wide skyscraper: 160×600
Large rectangle: 300x600
Mobile leaderboard: 320×50
Billboard: 970x250

Here are the Formatting Guidelines (WEB ADS): https://help.pixvane-example.com/hc/en-us/articles/583920174-Ad-Content-and-Format-Guidelines

No animation - photos to link back to the website.

Here is the website: https://www.kelbyrenews-example.com/

Please try to copy the look and feel.

Here are some words for the ad - feel free to use creative liberties if you have something better or need less words.

1. KELBY. Results - Not Recommendations.
2. KELBY. Transform Your Business By Transforming Your Core.
3. It's time for better results. It's time to change your management company. KELBY.
4. What company couldn't benefit from a "fresh set of eyes?" Talk to Kelby.
5. Talk to KELBY about what they can do for your bottom-line.

Target Market(s)

People who have already visited our website. These people will be private owners, REITs, or Private Equity people looking for a new management company for their underperforming asset.

Industry/Entity Type

Property Management

Font styles to use
Sans Serif

Colors
f37122
6b449b
33b8a4

Requirements
Must have
• logo - at least the "O" unless you can find other ways to pull it back to the website.
Nice to have
• Photos from kelbyrenews-example.com to remind the user what website we are when they are redirected - I purchased from lumbra photos off tilde grove.
Should not have
• Animation

```html
<!DOCTYPE html>
<html lang="en">
<head>
<meta charset="utf-8">
<title>KELBY Leaderboard Ad</title>
<link href="https://fonts.googleapis.com/css2?family=Roboto+Condensed:wght@600&display=swap" rel="stylesheet">
<style>
  :root {
    --text-purple: #5b2c83;
    --canvas-white: #ffffff;
    --paper-cream: #f4ead8;
    --paper-blue: #d9eef2;
    --paper-pink: #f6d7cf;
    --paper-yellow: #f5edb8;
    --wood-light: #e9e1d2;
  }
  html, body {
    margin: 0;
    padding: 0;
    overflow: hidden;
    background: var(--canvas-white);
  }
  .leaderboard {
    position: relative;
    display: block;
    width: 1200px;
    height: 148px;
    overflow: hidden;
    text-decoration: none;
    background: var(--canvas-white);
  }
  .hero-photo {
    position: absolute;
    top: 0;
    right: 0;
    width: 660px;
    height: 148px;
    background:
      radial-gradient(ellipse 120px 70px at 78% 20%, var(--paper-pink), transparent 70%),
      radial-gradient(ellipse 140px 80px at 62% 85%, var(--paper-yellow), transparent 70%),
      radial-gradient(ellipse 110px 90px at 92% 75%, var(--paper-blue), transparent 70%),
      radial-gradient(ellipse 150px 70px at 45% 25%, var(--paper-blue), transparent 70%),
      linear-gradient(90deg, var(--wood-light), var(--paper-cream));
  }
  .hero-fade {
    position: absolute;
    top: 0;
    right: 0;
    width: 660px;
    height: 148px;
    background: linear-gradient(90deg, var(--canvas-white) 0%, rgba(255,255,255,0.85) 35%, rgba(255,255,255,0.25) 75%, rgba(255,255,255,0.05) 100%);
  }
  .brand {
    position: absolute;
    left: 48px;
    top: 44px;
    display: flex;
    align-items: center;
    gap: 18px;
  }
  .brand-square {
    width: 22px;
    height: 22px;
    background: var(--text-purple);
  }
  .brand-name {
    font-family: "Roboto Condensed", sans-serif;
    font-weight: 600;
    font-size: 58px;
    line-height: 60px;
    letter-spacing: 1px;
    color: var(--text-purple);
  }
  .headline {
    position: absolute;
    left: 450px;
    top: 54px;
    margin: 0;
    font-family: "Roboto Condensed", sans-serif;
    font-weight: 600;
    font-size: 42px;
    line-height: 42px;
    letter-spacing: 1.2px;
    color: var(--text-purple);
    white-space: nowrap;
  }
</style>
</head>
<body>
  <a class="leaderboard" href="https://www.kelbyrenews-example.com/">
    <div class="hero-photo" role="img" aria-label="Pastel sticky notes scattered on a light wooden desk"></div>
    <div class="hero-fade"></div>
    <div class="brand">
      <span class="brand-square"></span>
      <span class="brand-name">KELBY</span>
    </div>
    <h1 class="headline">RESULTS - NOT RECOMMENDATIONS</h1>
  </a>
</body>
</html>
```